BrambleWorks business card

Looking for business card design that supports our company/software values. We have 2 logo designs at the moment but open to change if you think you can enhance the brand. Check out website www.brambleworks.com.au.

Target Market(s)

Education

Contact Information for Business Card

Name, title, mobile, email and website

Font styles to use
Sans Serif

Colors

Designer to choose colors to be used in the design.

Requirements
Must have
• BrambleWorks logo with tree and tagline on rear side with dark grey background colour

```html
<!DOCTYPE html>
<html lang="en">
<head>
<meta charset="utf-8">
<title>BrambleWorks business card</title>
<link rel="stylesheet" href="https://fonts.googleapis.com/css2?family=Lato:wght@400;700;900&display=swap">
<style>
  :root {
    --stage: #1e1e1e;
    --card-dark: #4a4a48;
    --card-light: #ffffff;
    --ink: #111111;
    --ink-soft: #555555;
    --leaf: #6cbf46;
    --white: #ffffff;
  }
  * { box-sizing: border-box; margin: 0; padding: 0; }
  html, body {
    width: 1200px;
    height: 780px;
    overflow: hidden;
    background: var(--stage);
    font-family: "Lato", "Segoe UI", sans-serif;
  }
  .stage {
    position: relative;
    width: 1200px;
    height: 780px;
  }
  .card {
    position: absolute;
    width: 600px;
    height: 343px;
    box-shadow: 0 18px 40px rgba(0, 0, 0, 0.55);
    overflow: hidden;
  }

  /* Rear side */
  .card--rear {
    left: 90px;
    top: 40px;
    background: var(--card-dark);
    color: var(--white);
  }
  .brand {
    position: absolute;
    left: 150px;
    top: 112px;
    display: flex;
    flex-direction: column;
  }
  .brand__row {
    display: flex;
    align-items: center;
    gap: 16px;
  }
  .brand__dot {
    width: 26px;
    height: 26px;
    border-radius: 50%;
    background: var(--leaf);
    flex: none;
  }
  .brand__name {
    font-weight: 400;
    font-size: 56px;
    letter-spacing: 1px;
    line-height: 1;
    color: var(--white);
  }
  .brand__rule {
    margin: 12px 0 6px 42px;
    height: 1px;
    width: 262px;
    background: var(--white);
  }
  .brand__tagline {
    margin-left: 48px;
    font-size: 19px;
    letter-spacing: 1px;
    color: var(--white);
  }

  /* Front side */
  .card--front {
    left: 510px;
    top: 397px;
    background: var(--card-light);
    color: var(--ink);
  }
  .contact {
    position: absolute;
    left: 42px;
    bottom: 38px;
  }
  .contact__name {
    font-weight: 900;
    font-size: 30px;
    letter-spacing: 0.5px;
    color: var(--ink);
  }
  .contact__title {
    font-size: 17px;
    color: var(--ink-soft);
    margin: 2px 0 14px;
  }
  .contact__list { list-style: none; }
  .contact__item {
    display: flex;
    align-items: center;
    gap: 14px;
    font-size: 17px;
    color: var(--ink);
    line-height: 1.65;
  }
  .contact__icon {
    width: 16px;
    height: 16px;
    flex: none;
  }
</style>
</head>
<body>
<main class="stage">

  <section class="card card--rear" aria-label="Card rear">
    <div class="brand">
      <div class="brand__row">
        <span class="brand__dot" aria-hidden="true"></span>
        <span class="brand__name">BrambleWorks</span>
      </div>
      <div class="brand__rule"></div>
      <div class="brand__tagline">Student Success Platform</div>
    </div>
  </section>

  <section class="card card--front" aria-label="Card front">
    <div class="contact">
      <h1 class="contact__name">JOHN SMITH</h1>
      <p class="contact__title">Founder &amp; CEO</p>
      <ul class="contact__list">
        <li class="contact__item">
          <svg class="contact__icon" viewBox="0 0 16 16" aria-hidden="true">
            <path d="M3.5 1.5l2.5 0 1 3.5-1.8 1.2a8 8 0 0 0 4.6 4.6L11 9l3.5 1v2.5c0 1-1 2-2 2A11 11 0 0 1 1.5 3.5c0-1 1-2 2-2z" fill="#111"/>
          </svg>
          123 456 7890
        </li>
        <li class="contact__item">
          <svg class="contact__icon" viewBox="0 0 16 16" aria-hidden="true">
            <rect x="1" y="3" width="14" height="10" fill="#111"/>
            <path d="M1 3l7 6 7-6" fill="none" stroke="#fff" stroke-width="1.2"/>
          </svg>
          lorem@yourwebsite.com
        </li>
        <li class="contact__item">
          <svg class="contact__icon" viewBox="0 0 16 16" aria-hidden="true">
            <circle cx="8" cy="8" r="6.5" fill="none" stroke="#111" stroke-width="1.4"/>
            <ellipse cx="8" cy="8" rx="3" ry="6.5" fill="none" stroke="#111" stroke-width="1"/>
            <path d="M1.5 8h13M2.5 5h11M2.5 11h11" stroke="#111" stroke-width="1"/>
          </svg>
          www.yourwebsite.com
        </li>
      </ul>
    </div>
  </section>

</main>
</body>
</html>
```